promotional flyer for Valtera Gym

we are after a double sided a5 leaflet to promote our gym, this is to go out to the general public to entice them into getting membership.

gym membership is £30 per month

it should also include the offer of - if you present this leaflet then there will be no joining fee

some of the features of the gym include

strength machines
cardio machines
functional area
sprung floor mat area

Target Market(s)

Adults 16+ who want to go to the gym and workout

Industry/Entity Type

Gym

Font styles to use
Other font styles liked:
• montserrat Regular

Requirements
Must have
• Clean on brand design
• use images supplied by us
Nice to have
• focus on an inclusive experience as the gym will be advertised to everyone
• should also use our "fitter, stronger, Healthier"

```html
<!DOCTYPE html>
<html lang="en">
<head>
<meta charset="utf-8">
<title>Valtera Gym – A5 Leaflet</title>
<link href="https://fonts.googleapis.com/css2?family=Oswald:wght@500;600&family=Montserrat:wght@300;400;500&family=Barlow:wght@300;400;500&display=swap" rel="stylesheet">
<style>
  :root {
    --orange: #f05a28;
    --slate: #4e5a65;
    --white: #ffffff;
    --ink: #3a3f45;
    --muted: #8a9097;
    --bell: #7d5f55;
    --backdrop: #e9e6e2;
  }
  * { margin: 0; padding: 0; box-sizing: border-box; }
  html, body { width: 1200px; height: 1200px; overflow: hidden; background: var(--backdrop); }
  .canvas { position: relative; width: 1200px; height: 1200px; }
  .page {
    position: absolute; top: 221px; width: 595px; height: 835px;
    transform: scale(0.9076); transform-origin: 0 0;
    background: var(--white); overflow: hidden;
    box-shadow: 0 6px 18px rgba(0,0,0,0.18);
  }
  .page--front { left: 40px; }
  .page--back { left: 620px; }
  .page__art { position: absolute; inset: 0; width: 595px; height: 835px; }

  .headline { position: absolute; left: 70px; top: 108px; font-family: "Oswald", sans-serif; font-weight: 600; line-height: 1; }
  .headline span { display: block; }
  .headline .hl-accent { color: var(--orange); font-size: 40px; margin-bottom: 8px; }
  .headline .hl-muted { color: var(--slate); font-size: 27px; margin-bottom: 8px; }
  .headline .hl-price { color: var(--orange); font-size: 35px; margin-bottom: 6px; }

  .brand { position: absolute; left: 68px; top: 462px; width: 262px; text-align: center; }
  .brand__name { display: flex; align-items: center; justify-content: center; gap: 10px;
    font-family: "Montserrat", sans-serif; font-weight: 500; font-size: 26px; color: var(--slate); }
  .brand__dot { width: 14px; height: 14px; border-radius: 50%; background: var(--slate); }
  .strapline { margin-top: 10px; font-family: "Montserrat", sans-serif; font-weight: 300; font-size: 13px; color: var(--muted); }

  .features { position: absolute; left: 78px; top: 580px; list-style: none; font-family: "Montserrat", sans-serif; font-weight: 300; font-size: 17px; color: var(--muted); }
  .features li { display: flex; align-items: center; gap: 8px; height: 24.5px; }
  .features svg { width: 20px; height: 10px; }

  .offer { position: absolute; right: 37px; top: 744px; text-align: right; font-family: "Oswald", sans-serif; font-weight: 500; font-size: 16.5px; line-height: 1.25; color: var(--white); }

  .contact { position: absolute; left: 78px; top: 603px; font-family: "Barlow", sans-serif; font-weight: 400; font-size: 8.6px; line-height: 1.4; color: var(--ink); }
  .contact p { margin-bottom: 9px; }
  .contact .indent { padding-left: 94px; }
  .phone { position: absolute; right: 44px; top: 718px; text-align: center; color: var(--white); font-family: "Barlow", sans-serif; }
  .phone__number { font-size: 28px; font-weight: 500; line-height: 1.1; }
  .phone__web { font-size: 14px; font-weight: 300; opacity: 0.85; }
</style>
</head>
<body>
<div class="canvas">

  <section class="page page--front" aria-label="Leaflet front">
    <svg class="page__art" viewBox="0 0 595 835" xmlns="http://www.w3.org/2000/svg">
      <defs>
        <linearGradient id="spinTones" x1="0" y1="0" x2="1" y2="1">
          <stop offset="0" stop-color="#3b3f4a"/><stop offset="0.5" stop-color="#6b5a5a"/><stop offset="1" stop-color="#8a5e3a"/>
        </linearGradient>
        <linearGradient id="machineTones" x1="0" y1="0" x2="1" y2="1">
          <stop offset="0" stop-color="#4a4f5c"/><stop offset="0.5" stop-color="#7a5560"/><stop offset="1" stop-color="#9a6a3e"/>
        </linearGradient>
        <g id="bell"><rect x="0" y="-9" width="6" height="18" rx="2"/><rect x="7" y="-13" width="7" height="26" rx="2"/><rect x="14" y="-2" width="52" height="4"/><rect x="66" y="-13" width="7" height="26" rx="2"/><rect x="74" y="-9" width="6" height="18" rx="2"/></g>
      </defs>
      <path class="slate-wave" fill="var(--slate)" d="M324,0 L595,0 L595,835 L0,835 C250,780 430,715 448,560 C458,470 400,420 332,390 C250,352 228,250 258,160 C278,95 298,45 324,0 Z"/>
      <g fill="var(--bell)">
        <use href="#bell" transform="translate(310,60)"/>
        <use href="#bell" transform="translate(452,112) scale(0.45)"/>
        <use href="#bell" transform="translate(278,190) scale(0.75)"/>
        <use href="#bell" transform="translate(460,190) scale(0.75)"/>
        <use href="#bell" transform="translate(410,698)"/>
        <use href="#bell" transform="translate(348,727) scale(0.45)"/>
      </g>
      <g fill="none" stroke="var(--orange)" stroke-width="1.6">
        <polygon points="394,124 519,249 394,374 269,249"/>
        <polygon points="394,130 513,249 394,368 275,249"/>
        <polygon points="466,285 601,420 466,555 331,420"/>
        <polygon points="466,295 591,420 466,545 341,420"/>
        <polygon points="466,305 581,420 466,535 351,420"/>
      </g>
      <polygon role="img" aria-label="Photo: two members riding spin bikes in the studio" fill="url(#spinTones)" points="394,104 530,240 394,376 258,240"/>
      <polygon role="img" aria-label="Photo: member training on a leg machine" fill="url(#machineTones)" points="466,338 592,464 466,590 340,464"/>
    </svg>

    <h1 class="headline">
      <span class="hl-accent">Gym</span>
      <span class="hl-muted">membership is</span>
      <span class="hl-price">£30 per</span>
      <span class="hl-muted">month</span>
    </h1>

    <div class="brand">
      <div class="brand__name"><span class="brand__dot"></span>Valtera Gym</div>
      <p class="strapline">Fitter, stronger and healthier</p>
    </div>

    <ul class="features">
      <li><svg viewBox="0 0 20 10"><rect x="0" y="2" width="4" height="6" fill="var(--orange)"/><rect x="4" y="4" width="12" height="2" fill="var(--orange)"/><rect x="16" y="2" width="4" height="6" fill="var(--orange)"/></svg>strength machines</li>
      <li><svg viewBox="0 0 20 10"><rect x="0" y="2" width="4" height="6" fill="var(--orange)"/><rect x="4" y="4" width="12" height="2" fill="var(--orange)"/><rect x="16" y="2" width="4" height="6" fill="var(--orange)"/></svg>cardio machines</li>
      <li><svg viewBox="0 0 20 10"><rect x="0" y="2" width="4" height="6" fill="var(--orange)"/><rect x="4" y="4" width="12" height="2" fill="var(--orange)"/><rect x="16" y="2" width="4" height="6" fill="var(--orange)"/></svg>functional area</li>
      <li><svg viewBox="0 0 20 10"><rect x="0" y="2" width="4" height="6" fill="var(--orange)"/><rect x="4" y="4" width="12" height="2" fill="var(--orange)"/><rect x="16" y="2" width="4" height="6" fill="var(--orange)"/></svg>sprung floor mat area</li>
    </ul>

    <p class="offer">If you present this leaflet then there<br>will be no joining fee</p>
  </section>

  <section class="page page--back" aria-label="Leaflet back">
    <svg class="page__art" viewBox="0 0 595 835" xmlns="http://www.w3.org/2000/svg">
      <defs>
        <linearGradient id="toneA" x1="0" y1="0" x2="1" y2="1"><stop offset="0" stop-color="#3b3f4a"/><stop offset="1" stop-color="#8a5e3a"/></linearGradient>
        <linearGradient id="toneB" x1="0" y1="0" x2="1" y2="1"><stop offset="0" stop-color="#6a5a8a"/><stop offset="1" stop-color="#3e3a3c"/></linearGradient>
        <linearGradient id="toneC" x1="0" y1="0" x2="1" y2="1"><stop offset="0" stop-color="#4a4f5c"/><stop offset="1" stop-color="#9a6a3e"/></linearGradient>
        <linearGradient id="toneD" x1="0" y1="0" x2="1" y2="1"><stop offset="0" stop-color="#6d3a6a"/><stop offset="0.6" stop-color="#4a5a3e"/><stop offset="1" stop-color="#3a3a3a"/></linearGradient>
        <linearGradient id="toneE" x1="0" y1="0" x2="1" y2="1"><stop offset="0" stop-color="#b04a30"/><stop offset="1" stop-color="#3a302c"/></linearGradient>
      </defs>
      <path class="orange-wave" fill="var(--orange)" d="M330,0 L595,0 L595,835 L18,835 C260,780 445,660 456,510 C462,420 420,385 372,372 L330,0 Z"/>
      <polygon role="img" aria-label="Photo: members on spin bikes" fill="url(#toneA)" points="158,48 283,173 158,298 33,173"/>
      <polygon role="img" aria-label="Photo: member using a shoulder press" fill="url(#toneB)" points="358,-5 478,115 358,235 238,115"/>
      <polygon role="img" aria-label="Photo: member training on a leg machine" fill="url(#toneC)" points="483,125 603,245 483,365 363,245"/>
      <polygon role="img" aria-label="Photo: member lifting dumbbells in the functional area" fill="url(#toneD)" points="308,190 433,315 308,440 183,315"/>
      <polygon role="img" aria-label="Photo: member with dumbbells in the weights room" fill="url(#toneE)" points="126,290 251,415 126,540 1,415"/>
    </svg>

    <div class="contact">
      <p>Address - Valtera Gym, Unit 4 Harbour Row, Linden Avenue,<br>Westmere, West Sussex, BN99 4QT</p>
      <p>Email enquiries@valteragym.co.uk</p>
      <p>Opening hours 6am - 10pm mon to Fri and<br><span class="indent">7am to 7pm Saturday and Sunday</span></p>
    </div>

    <div class="phone">
      <div class="phone__number">Tel 01632 960482</div>
      <div class="phone__web">www.valteragym.co.uk</div>
    </div>
  </section>

</div>
</body>
</html>
```